Design of business signage for outside store front

We need signage designed for outside a store front.  We already have a logo, colours and font that we would like to use but would like some ideas as regards layout/design of the signage.  The final product will be for the use of the installer to produce and install the signage.  Attached are files with our logo and font and a picture of the current signage which needs to be replaced.  The size and shape of the signage will be the same as the current signage, its just the design/layout that we would like changed.
N.B. We would like two versions if possible, one with the web address and one without the web address to see what they look like.

```html
<!DOCTYPE html>
<html lang="en">
<head>
<meta charset="utf-8">
<title>Relish Iberia – Storefront Sign</title>
<link rel="stylesheet" href="https://fonts.googleapis.com/css2?family=Sorts+Mill+Goudy&family=Work+Sans:wght@400&display=swap">
<style>
  :root {
    --backdrop: #878787;
    --maroon: #8a2433;
    --maroon-deep: #2e0d12;
    --gold: #fed420;
    --gold-soft: #f6e27a;
    --cream: #fbf1c9;
    --ink: #0d0d0d;
    --paper: #ffffff;
  }
  * { margin: 0; padding: 0; box-sizing: border-box; }
  html, body {
    width: 1200px;
    height: 690px;
    overflow: hidden;
    background: var(--backdrop);
  }
  .sign {
    position: absolute;
    left: 74px;
    top: 116px;
    width: 1053px;
    height: 459px;
    background: linear-gradient(180deg, var(--paper) 0%, var(--paper) 35%, var(--cream) 100%);
    box-shadow: 5px 6px 6px rgba(0, 0, 0, 0.4);
    overflow: hidden;
  }
  .sign__panel {
    position: absolute;
    inset: 0;
    width: 1053px;
    height: 459px;
  }
  .sign__emblem {
    position: absolute;
    left: 38px;
    top: 40px;
    width: 276px;
    height: 396px;
    border-radius: 46% 40% 44% 40%;
    background: radial-gradient(ellipse at 45% 50%, rgba(255, 255, 255, 0.55) 0%, rgba(246, 214, 70, 0.45) 45%, rgba(138, 36, 51, 0) 75%);
  }
  .sign__doodles {
    position: absolute;
    left: 352px;
    top: 330px;
    width: 701px;
    height: 129px;
    background: linear-gradient(180deg, rgba(254, 212, 32, 0) 0%, rgba(254, 212, 32, 0.22) 55%, rgba(254, 212, 32, 0.3) 100%);
  }
  .sign__name {
    position: absolute;
    left: 499px;
    top: 66px;
    width: 506px;
    font-family: "Sorts Mill Goudy", "Goudy Old Style", serif;
    color: var(--maroon);
  }
  .sign__name-top,
  .sign__name-bottom {
    display: flex;
    justify-content: space-between;
    line-height: 1;
  }
  .sign__name-top { font-size: 132px; height: 100px; }
  .sign__name-bottom { font-size: 84px; margin-top: 25px; }
  .sign__band {
    position: absolute;
    left: 480px;
    top: 288px;
    width: 573px;
    height: 54px;
    background: linear-gradient(90deg, rgba(254, 212, 32, 0) 0%, rgba(254, 224, 90, 0.55) 25%, var(--gold-soft) 60%, var(--gold) 100%);
    transform: skewY(-0.6deg);
  }
  .sign__tagline {
    position: absolute;
    left: 505px;
    top: 290px;
    width: 510px;
    font-family: "Work Sans", Helvetica, Arial, sans-serif;
    font-size: 39px;
    letter-spacing: 0.075em;
    color: var(--ink);
    white-space: nowrap;
    line-height: 50px;
  }
</style>
</head>
<body>
  <section class="sign" aria-label="Relish Iberia storefront sign">
    <svg class="sign__panel" viewBox="0 0 1053 459" aria-hidden="true">
      <defs>
        <linearGradient id="maroonFade" x1="0" y1="0" x2="1" y2="0">
          <stop offset="0" stop-color="#8a2433"/>
          <stop offset="0.55" stop-color="#6a1c28"/>
          <stop offset="1" stop-color="#2e0d12"/>
        </linearGradient>
        <linearGradient id="goldFade" x1="0" y1="0" x2="0" y2="1">
          <stop offset="0" stop-color="#fed420"/>
          <stop offset="1" stop-color="#d9b93a"/>
        </linearGradient>
        <linearGradient id="creamFade" x1="0" y1="0" x2="0" y2="1">
          <stop offset="0" stop-color="#ffffff"/>
          <stop offset="0.5" stop-color="#f8e9a8"/>
          <stop offset="1" stop-color="#fbefc2"/>
        </linearGradient>
      </defs>
      <path class="sign__swoosh-outer" d="M0 0 H404 C470 70 490 170 445 260 C410 330 350 400 290 459 H0 Z" fill="url(#creamFade)"/>
      <path class="sign__swoosh-gold" d="M0 0 H364 C430 60 448 150 420 240 C395 320 340 400 290 459 H0 Z" fill="url(#goldFade)"/>
      <path class="sign__field" d="M0 0 H317 C390 60 420 140 405 220 C390 310 340 390 288 459 H0 Z" fill="url(#maroonFade)"/>
    </svg>

    <div class="sign__emblem" role="img" aria-label="Brand emblem: a flamenco dancer silhouette wrapped in a golden ribbon"></div>
    <div class="sign__doodles" role="img" aria-label="Line drawings of Spanish foods: bowls of soup, tart slice, olives, bread, shellfish and paella"></div>

    <h1 class="sign__name">
      <span class="sign__name-top"><span>R</span><span>E</span><span>L</span><span>I</span><span>S</span><span>H</span></span>
      <span class="sign__name-bottom"><span>I</span><span>B</span><span>E</span><span>R</span><span>I</span><span>A</span></span>
    </h1>

    <div class="sign__band"></div>
    <p class="sign__tagline">Spanish Artisan Foods</p>
  </section>
</body>
</html>
```